Looking for a Lumora Book Cover

My book has been online for a while and I am now looking for a professional cover for it as it has been very well received.

You can view the book here and all the details about it:

https://www.pagevaultshop.example/dp/X7Q2KRMTPL#readerNotes

Not sure what I am looking for as a design, just open to your ideas.

I want something different that will stand out please.

Thanks
Owen

```html
<!DOCTYPE html>
<html lang="en">
<head>
<meta charset="utf-8">
<title>Ashes and Awakening — Book Cover</title>
<link rel="stylesheet" href="https://fonts.googleapis.com/css2?family=Bebas+Neue&family=Oswald:wght@300;400;600;700&display=swap">
<style>
  :root {
    --skin-deep: #2a1712;
    --skin-mid: #5a3024;
    --skin-warm: #8a4a38;
    --shadow-teal: #1a2a2e;
    --ink: #0c0c0d;
    --paper: #ffffff;
    --accent-red: #e0201f;
    --band: #1c1414;
  }
  html, body {
    margin: 0;
    padding: 0;
    width: 800px;
    height: 1200px;
    overflow: hidden;
    background: var(--ink);
  }
  .cover {
    position: relative;
    width: 800px;
    height: 1200px;
    overflow: hidden;
  }
  .cover-photo {
    position: absolute;
    inset: 0;
    background:
      radial-gradient(ellipse 55% 40% at 30% 30%, var(--skin-warm) 0%, transparent 70%),
      radial-gradient(ellipse 50% 45% at 25% 65%, var(--skin-mid) 0%, transparent 75%),
      linear-gradient(90deg, var(--skin-deep) 0%, var(--skin-mid) 45%, #3a2a28 70%, var(--shadow-teal) 100%);
  }
  .cover-photo::after {
    content: "";
    position: absolute;
    inset: 0;
    background: linear-gradient(180deg, rgba(0,0,0,0.25) 0%, transparent 30%, transparent 70%, rgba(0,0,0,0.45) 100%);
  }
  .cover-type {
    position: absolute;
    inset: 0;
  }
  .title-line {
    font-family: "Bebas Neue", "Oswald", sans-serif;
    fill: var(--paper);
  }
  .tagline-band { fill: var(--band); }
  .tagline {
    font-family: "Oswald", sans-serif;
    font-weight: 600;
    fill: var(--accent-red);
  }
  .subtitle-rule { stroke: var(--accent-red); stroke-width: 3; }
  .subtitle {
    font-family: "Oswald", sans-serif;
    font-weight: 300;
    fill: var(--paper);
  }
  .author {
    font-family: "Oswald", sans-serif;
    font-weight: 600;
    fill: var(--paper);
  }
</style>
</head>
<body>
  <main class="cover">
    <div class="cover-photo" role="img" aria-label="Close-up portrait photograph in warm brown tones with grey clay markings, fading to a dark teal background"></div>

    <svg class="cover-type" width="800" height="1200" viewBox="0 0 800 1200" xmlns="http://www.w3.org/2000/svg">
      <text class="title-line" x="102" y="658" font-size="256" textLength="597" lengthAdjust="spacingAndGlyphs">ASHES AND</text>

      <rect class="tagline-band" x="102" y="665" width="596" height="37"/>
      <text class="tagline" x="120" y="693" font-size="23" textLength="560" lengthAdjust="spacingAndGlyphs">A TRIBUTE TO HERITAGE, HARDSHIP AND HARD-WON TRIUMPH</text>

      <text class="title-line" x="102" y="895" font-size="256" textLength="596" lengthAdjust="spacingAndGlyphs">AWAKENING</text>

      <line class="subtitle-rule" x1="206" y1="970" x2="206" y2="1040"/>
      <line class="subtitle-rule" x1="593" y1="970" x2="593" y2="1040"/>
      <text class="subtitle" x="225" y="1000" font-size="21" textLength="350" lengthAdjust="spacingAndGlyphs">The Story, Defiance and Brilliance of</text>
      <text class="subtitle" x="225" y="1028" font-size="21" textLength="350" lengthAdjust="spacingAndGlyphs">African Peoples at Home and Across the World</text>

      <text class="author" x="105" y="1160" font-size="72" textLength="592" lengthAdjust="spacingAndGlyphs">DESMOND ASHBURY</text>
    </svg>
  </main>
</body>
</html>
```